I need a business Card Design for my practice , i am clinical herbalist. I am a herbalist specializing in Lyme disease, autism, autoimmune diseases, difficult to cure diseasesDifficult to cure diseases. In my innovative practice i link traditional medicine, herbs with science, immunologu ,pharmacology.

Industry/Entity Type

Business

Contact Information for Business Card

My company name : OŚRODEK ZIELNIK
My name : Piotr Kaleta
Name of my profession : Fitoterapeuta
In Polish language Fitoterapeuta is Herbalist .

e-mail: piotrkaleta@osrodekzielnik.com
www.osrodek-zielnik.pl
phone : 604 587 231
My company adress : Dąbrowa Sitnicka 41 , 38-415 Brzozówka
I dont have logo .

Requirements
Nice to have
• My company

```html
<!DOCTYPE html>
<html lang="pl">
<head>
<meta charset="utf-8">
<title>Ośrodek Zielnik – wizytówka</title>
<link href="https://fonts.googleapis.com/css2?family=Cinzel:wght@500;600&family=Montserrat:wght@400;500;600;700&display=swap" rel="stylesheet">
<style>
  :root {
    --page: #e9ebe6;
    --green: #557f3a;
    --green-light: #8cba34;
    --white: #ffffff;
    --shadow: rgba(0, 0, 0, 0.18);
  }
  * { margin: 0; padding: 0; box-sizing: border-box; }
  html, body {
    width: 1200px;
    height: 864px;
    overflow: hidden;
    background: var(--page);
  }
  .sheet {
    width: 1200px;
    height: 864px;
    display: flex;
    align-items: center;
    justify-content: center;
    gap: 40px;
  }
  .card {
    position: relative;
    width: 540px;
    height: 309px;
    border-radius: 18px;
    overflow: hidden;
    box-shadow: 0 10px 28px var(--shadow);
  }

  /* Front */
  .card--front {
    background: var(--green);
    color: var(--white);
  }
  .front-title {
    position: absolute;
    top: 114px;
    left: 0;
    right: 0;
    text-align: center;
    font-family: "Cinzel", serif;
    font-weight: 600;
    font-size: 35px;
    letter-spacing: 1px;
  }
  .front-web {
    position: absolute;
    bottom: 34px;
    left: 0;
    right: 0;
    text-align: center;
    font-family: "Montserrat", sans-serif;
    font-size: 11px;
    letter-spacing: 0.3px;
  }

  /* Back */
  .card--back { background: var(--white); }
  .back-swoosh {
    position: absolute;
    inset: 0;
    width: 100%;
    height: 100%;
  }
  .back-title {
    position: absolute;
    top: 38px;
    right: 30px;
    font-family: "Cinzel", serif;
    font-weight: 600;
    font-size: 31px;
    color: var(--green);
    letter-spacing: 0.5px;
  }
  .contact {
    position: absolute;
    left: 34px;
    top: 144px;
    color: var(--white);
    font-family: "Montserrat", sans-serif;
  }
  .contact-name { font-weight: 700; font-size: 21px; line-height: 1.1; }
  .contact-role { font-size: 12px; margin-top: 2px; }
  .contact-company { font-weight: 700; font-size: 12px; margin-top: 12px; }
  .contact-address { font-size: 12px; margin-top: 1px; }
  .contact-list { list-style: none; margin-top: 10px; }
  .contact-list li {
    display: flex;
    align-items: center;
    gap: 7px;
    font-size: 12px;
    line-height: 1.5;
  }
  .contact-list svg { width: 12px; height: 12px; flex: none; }
</style>
</head>
<body>
<main class="sheet">

  <section class="card card--front" aria-label="Przód wizytówki">
    <h1 class="front-title">Ośrodek Zielnik</h1>
    <p class="front-web">www.osrodek-zielnik.pl</p>
  </section>

  <section class="card card--back" aria-label="Tył wizytówki">
    <svg class="back-swoosh" viewBox="0 0 540 309" preserveAspectRatio="none" aria-hidden="true">
      <path d="M200,103 C330,110 430,190 500,309 L482,309 C410,200 320,125 200,103 Z" fill="var(--green-light)"/>
      <path d="M0,112 C180,96 380,130 478,309 L0,309 Z" fill="var(--white)"/>
      <path d="M0,116 C180,100 370,132 470,309 L0,309 Z" fill="var(--green)"/>
    </svg>

    <h2 class="back-title">Ośrodek Zielnik</h2>

    <div class="contact">
      <p class="contact-name">Piotr Kaleta</p>
      <p class="contact-role">Fitoterapeuta</p>
      <p class="contact-company">OŚRODEK ZIELNIK</p>
      <p class="contact-address">Dąbrowa Sitnicka 41, 38-415 Brzozówka</p>
      <ul class="contact-list">
        <li>
          <svg viewBox="0 0 24 24" aria-hidden="true"><path fill="currentColor" d="M6.6 10.8a15.1 15.1 0 0 0 6.6 6.6l2.2-2.2c.3-.3.7-.4 1-.2 1.1.4 2.3.6 3.6.6.6 0 1 .4 1 1V20c0 .6-.4 1-1 1A17 17 0 0 1 3 4c0-.6.4-1 1-1h3.5c.6 0 1 .4 1 1 0 1.3.2 2.5.6 3.6.1.3 0 .7-.2 1z"/></svg>
          604 587 231
        </li>
        <li>
          <svg viewBox="0 0 24 24" aria-hidden="true"><path fill="currentColor" d="M2 5h20v14H2z M4 7v.4l8 5.2 8-5.2V7z" fill-rule="evenodd"/></svg>
          piotrkaleta@osrodekzielnik.com
        </li>
        <li>
          <svg viewBox="0 0 24 24" aria-hidden="true"><g fill="none" stroke="currentColor" stroke-width="2"><circle cx="12" cy="12" r="9.5"/><ellipse cx="12" cy="12" rx="4" ry="9.5"/><path d="M2.5 12h19M4 7h16M4 17h16"/></g></svg>
          www.osrodek-zielnik.pl
        </li>
      </ul>
    </div>
  </section>

</main>
</body>
</html>
```